Print and E-book Personal Injury Front and Back Book Cover

I need a book cover for a personal injury law firm book titled "Rising Past the Wreckage" with the subtitle "A Plain Guide for Harmed Readers." The book cover should have an image. This isas a lead generation book designed to be give to potential clients to have them sign as new clients.

Target Market(s)

Potential New Clients Looking For a Personal Injury Attorney

Industry/Entity Type

Legal

Requirements
Must have
• Title and some type of image or images

```html
<!DOCTYPE html>
<html lang="en">
<head>
<meta charset="utf-8">
<title>Rising Past the Wreckage — Cover Wrap</title>
<link rel="stylesheet" href="https://fonts.googleapis.com/css2?family=Cinzel:wght@500;600&family=Oswald:wght@600&family=Lato:wght@400&display=swap">
<style>
  :root {
    --page: #ffffff;
    --ink: #000000;
    --gold: #d3b45c;
    --gold-deep: #a98a3a;
    --body-text: #e9e4d6;
    --photo-dark: #141210;
    --photo-wood: #6b4524;
    --photo-blue: #2c3644;
  }
  * { margin: 0; padding: 0; box-sizing: border-box; }
  html, body { width: 1200px; height: 288px; overflow: hidden; background: var(--page); }
  .stage { position: relative; width: 1200px; height: 288px; }
  .cover-wrap {
    position: absolute; left: 390px; top: 0;
    width: 420px; height: 288px;
    display: flex; background: var(--ink);
  }
  .gold {
    color: var(--gold);
    background: linear-gradient(180deg, #ecd58f 0%, var(--gold) 45%, var(--gold-deep) 100%);
    -webkit-background-clip: text; background-clip: text;
    -webkit-text-fill-color: transparent;
  }
  .serif { font-family: "Cinzel", serif; font-weight: 600; }
  .condensed { font-family: "Oswald", sans-serif; font-weight: 600; }

  /* back cover */
  .back-cover { width: 201px; height: 288px; position: relative; text-align: center; }
  .back-title { position: absolute; top: 28px; left: 0; right: 0; line-height: 0.92; }
  .back-title .line { display: block; font-size: 19px; }
  .back-title .line.condensed { font-size: 18px; letter-spacing: 0.2px; }
  .back-subtitle { position: absolute; top: 82px; left: 0; right: 0; font-size: 7.6px; line-height: 1.15; }
  .blurb {
    position: absolute; left: 19px; width: 155px;
    font-family: "Lato", sans-serif; font-size: 5px; line-height: 10.7px;
    color: var(--body-text); text-align: justify; text-align-last: center;
  }
  .blurb.first { top: 102px; }
  .blurb.second { top: 187px; }

  /* spine */
  .spine {
    width: 27px; height: 288px; position: relative;
    display: flex; justify-content: center;
  }
  .spine-text {
    writing-mode: vertical-rl; margin-top: 16px;
    font-size: 11.5px; white-space: nowrap; letter-spacing: 0.3px;
  }
  .spine-text .condensed { font-size: 11px; }
  .spine-author { margin-left: 0; margin-top: 14px; font-size: 9px; }

  /* front cover */
  .front-cover { width: 192px; height: 288px; position: relative; overflow: hidden; text-align: center; }
  .cover-photo {
    position: absolute; inset: 0;
    background:
      radial-gradient(ellipse 60% 30% at 55% 78%, var(--photo-wood) 0%, transparent 75%),
      radial-gradient(ellipse 50% 40% at 70% 25%, var(--photo-blue) 0%, transparent 80%),
      linear-gradient(180deg, #1e2127 0%, var(--photo-dark) 45%, #3a2614 72%, #1a110a 100%);
  }
  .front-subtitle { position: absolute; top: 19px; left: 0; right: 0; font-size: 8.6px; line-height: 1.05; }
  .front-title { position: absolute; top: 44px; left: 0; right: 0; line-height: 0.9; }
  .front-title .line { display: block; font-size: 36px; }
  .front-title .line.small { font-size: 32px; }
  .front-title .line.condensed { font-size: 27px; line-height: 1.05; letter-spacing: 0.2px; }
  .front-author { position: absolute; top: 254px; left: 0; right: 0; font-size: 12px; letter-spacing: 0.4px; }
</style>
</head>
<body>
<main class="stage">
  <div class="cover-wrap">
    <section class="back-cover">
      <h2 class="back-title">
        <span class="line serif gold">Rising</span>
        <span class="line serif gold">Past</span>
        <span class="line condensed gold">THE WRECKAGE</span>
      </h2>
      <p class="back-subtitle serif gold">A PLAIN GUIDE FOR<br>HARMED READERS</p>
      <p class="blurb first">Lorem ipsum dolor sit amet, consectetur adipiscing elit, sed do eiusmod tempor incididunt ut labore et dolore magna aliqua. Quis ipsum suspendisse ultrices gravida. Risus commodo viverra maecenas accumsan lacus vel facilisis. Lorem ipsum dolor sit amet, consectetur adipiscing elit, sed do eiusmod tempor incididunt ut labore et dolore magna aliqua. Quis ipsum suspendisse ultrices gravida. Risus commodo viverra maecenas accumsan lacus vel facilisis.</p>
      <p class="blurb second">Lorem ipsum dolor sit amet, consectetur adipiscing elit, sed do eiusmod tempor incididunt ut labore et dolore magna aliqua. Quis ipsum suspendisse ultrices gravida. Risus commodo viverra maecenas accumsan lacus vel facilisis. Lorem ipsum dolor sit amet, consectetur adipiscing elit, sed do eiusmod tempor incididunt ut labore et dolore magna aliqua. Quis ipsum suspendisse ultrices gravida. Risus commodo viverra maecenas accumsan lacus vel facilisis.</p>
    </section>

    <section class="spine">
      <p class="spine-text">
        <span class="serif gold">RISING PAST </span><span class="condensed gold">THE WRECKAGE</span>
        <span class="spine-author serif gold">&nbsp;&nbsp;&nbsp;AUTHOR NAME</span>
      </p>
    </section>

    <section class="front-cover">
      <div class="cover-photo" role="img" aria-label="Photograph of a wooden judge's gavel on a desk with a lawyer in a suit blurred in the background"></div>
      <p class="front-subtitle serif gold">A PLAIN GUIDE FOR<br>HARMED READERS</p>
      <h1 class="front-title">
        <span class="line serif gold">RISING</span>
        <span class="line small serif gold">PAST</span>
        <span class="line condensed gold">THE WRECKAGE</span>
      </h1>
      <p class="front-author serif gold">AUTHOR NAME</p>
    </section>
  </div>
</main>
</body>
</html>
```